Quiver Upcoming Gigs

One page graphic with my upcoming dates. Logo and photo attached, and sample from last flyer. Text:

QUIVER

UPCOMING DATES

3/26/18 Velvet Grotto (Las Vegas, NV)

4/1/18 Lantern Hall 2847 M St (Sac, CA)

4/8/18 Blue Heron (Sac, CA)

5/5/18 Open Lanes @ Silver Otter (Sac, CA)

5/10/18 Dunmore Fine Gallery (Sac, CA)

5/11/18 Bas Rive @ Cafe du Pont (Sac, CA)

5/27/18 Sunloft LBW @ Vox (Sac, CA)

Save The Date: 9/21/18 Moonweaver Festival (Puerto Nuevo, MX)

pulsepage.net/quiver530

Target Market(s)

House/Electronic Music

Industry/Entity Type

Night Club

Font styles to use
Sans Serif

Colors

Designer to choose colors to be used in the design.

Requirements
Must have
• Quiver logo or something that looks good instead. Prefer photo to be in but not necessary.
Nice to have

```html
<!DOCTYPE html>
<html lang="en">
<head>
<meta charset="utf-8">
<title>Quiver Upcoming Dates</title>
<link href="https://fonts.googleapis.com/css2?family=Exo+2:wght@700&family=Lato:wght@400&family=Russo+One&display=swap" rel="stylesheet">
<style>
  :root {
    --page: #e6e6e8;
    --ink: #050507;
    --blue: #1334b0;
    --blue-bright: #1a45d6;
    --white: #ffffff;
    --gold: #f2b630;
    --photo-violet: #5a2fd0;
    --photo-magenta: #c0306a;
    --photo-deep: #1a0b22;
  }
  * { margin: 0; padding: 0; box-sizing: border-box; }
  html, body { width: 1200px; height: 1200px; overflow: hidden; background: var(--page); }
  .flyer {
    position: absolute; left: 0; top: 286px;
    width: 1200px; height: 627px;
    background: var(--ink); overflow: hidden;
    font-family: "Lato", sans-serif; color: var(--white);
  }
  .artist-photo {
    position: absolute; right: 0; top: 0; width: 640px; height: 100%;
    background:
      radial-gradient(ellipse at 22% 18%, rgba(120,70,255,.75), transparent 55%),
      radial-gradient(ellipse at 60% 55%, rgba(220,60,140,.55), transparent 60%),
      radial-gradient(ellipse at 70% 90%, rgba(190,40,80,.6), transparent 55%),
      linear-gradient(160deg, var(--photo-violet) 0%, var(--photo-deep) 45%, var(--photo-magenta) 100%);
  }
  .artist-photo::after {
    content: ""; position: absolute; inset: 0;
    background: linear-gradient(90deg, var(--ink) 0%, rgba(5,5,7,.6) 18%, transparent 40%);
  }
  .logo {
    position: absolute; left: 37px; top: 14px;
    font-family: "Russo One", sans-serif; font-weight: 400;
    font-size: 132px; line-height: 1; letter-spacing: 0;
    color: var(--blue);
    transform: scaleX(0.84); transform-origin: left top;
    white-space: nowrap;
  }
  .heading {
    position: absolute; left: 37px; top: 164px;
    font-family: "Exo 2", sans-serif; font-weight: 700; font-size: 27px;
    letter-spacing: .3px;
  }
  .dates { position: absolute; left: 37px; top: 208px; list-style: none; }
  .gig { display: flex; align-items: center; height: 48.5px; }
  .gig-date {
    position: relative; width: 118px; height: 40px; margin-right: 36px;
    background: var(--blue);
    font-family: "Exo 2", sans-serif; font-weight: 700; font-size: 23px;
    line-height: 40px; padding-left: 11px;
  }
  .gig-date::after {
    content: ""; position: absolute; right: -20px; top: 0;
    border-left: 20px solid var(--blue-bright);
    border-top: 20px solid transparent; border-bottom: 20px solid transparent;
  }
  .gig-venue { font-size: 21.5px; }
  .city { color: var(--gold); }
  .save-date {
    position: absolute; left: 37px; top: 558px;
    display: flex; align-items: center; font-size: 21px;
  }
  .save-label { font-family: "Exo 2", sans-serif; font-weight: 700; margin-right: 4px; }
  .save-tag {
    position: relative; background: var(--blue); padding: 0 6px; margin-right: 18px;
    font-family: "Exo 2", sans-serif; font-weight: 700; line-height: 30px;
  }
  .save-tag::after {
    content: ""; position: absolute; right: -12px; top: 0;
    border-left: 12px solid var(--blue);
    border-top: 15px solid transparent; border-bottom: 15px solid transparent;
  }
  .social {
    position: absolute; right: 34px; top: 558px;
    display: flex; align-items: center; gap: 14px; font-size: 24px; line-height: 30px;
  }
  .social-dot { width: 24px; height: 24px; border-radius: 50%; background: var(--blue-bright); }
</style>
</head>
<body>
<main class="flyer">
  <div class="artist-photo" role="img" aria-label="Photo of the DJ performing at turntables under purple and pink club lights"></div>

  <h1 class="logo">QUIVER</h1>
  <h2 class="heading">QUIVER UPCOMING DATES</h2>

  <ul class="dates">
    <li class="gig"><span class="gig-date">3/26/18</span><span class="gig-venue">Velvet Grotto <span class="city">(Las Vegas, NV)</span></span></li>
    <li class="gig"><span class="gig-date">4/1/18</span><span class="gig-venue">Lantern Hall 2847 M St <span class="city">(Sac, CA)</span></span></li>
    <li class="gig"><span class="gig-date">4/8/18</span><span class="gig-venue">Blue Heron <span class="city">(Sac, CA)</span></span></li>
    <li class="gig"><span class="gig-date">5/5/18</span><span class="gig-venue">Open Lanes @ Silver Otter <span class="city">(Sac, CA)</span></span></li>
    <li class="gig"><span class="gig-date">5/10/18</span><span class="gig-venue">Dunmore Fine Gallery <span class="city">(Sac, CA)</span></span></li>
    <li class="gig"><span class="gig-date">5/11/18</span><span class="gig-venue">Bas Rive @ Cafe du Pont <span class="city">(Sac, CA)</span></span></li>
    <li class="gig"><span class="gig-date">5/27/18</span><span class="gig-venue">Sunloft LBW @ Vox <span class="city">(Sac, CA)</span></span></li>
  </ul>

  <p class="save-date">
    <span class="save-label">SAVE THE DATE:</span>
    <span class="save-tag">9/21/18</span>
    <span>Moonweaver Festival <span class="city">(Puerto Nuevo, MX)</span></span>
  </p>

  <p class="social"><span class="social-dot"></span><span>pulsepage.net/quiver530</span></p>
</main>
</body>
</html>
```